Fern Acupuncture Business Card Design

I would like a business card design for my acupuncture business which is based from 2 practices in Melbourne, Australia.

The front of the card should include:

*The Logo
* Name - Marnie Dobrowen (B.App.Sc.(TCM), Dip.Rem.Mass.). (I would like the letters after my name in slightly smaller font)
* Mobile number - 0491 570 313
* Web address - www.fernacupuncture-demo.com.au

On the back of the card I would somehow like to fit my 2 clinic addresses in. They are:

The Quiet Grove & Renewal Studio
842 Brindle St, Camberwell VIC 3124
Ph: 1300 482 177

Wattle Lane Integrative & Restorative Care Clinic
19 Ostler Rd, Malvern East VIC 3145
Ph: (03) 9018 4472

If there is space, I'd also like to add to the back of the card - Next Appointment............................ (or something along those lines).

Thanks and happy designing!

Target Market(s)

Health consumers, and colleagues in the health industry

Industry/Entity Type

Clinic

Contact Information for Business Card

as above in brief

Requirements
Must have
• I've seen some ok designs coming in, however I'd like to avoid the generic look with the added curved line details etc. I don't particularly need extra patterns added to the card. I'd prefer it to look quite clean and simple, and using more earthy colours (I'm not super keen on the lime green that a lot of designs seem to include. I don't mind the full black or white look, (obviously the back side needs to be a lighter colour to allow me to write appointment details on it). I also quite like the idea of the background looking like brown recycled paper (just an idea - that's not 100% necessary).
Nice to have
• I have an idea that I could have the main flower part of the logo printed as metallic.
Should not have
• Generic patterns and too much added detail.

```html
<!DOCTYPE html>
<html lang="en">
<head>
<meta charset="utf-8">
<title>Fern Acupuncture Business Card Concepts</title>
<link rel="stylesheet" href="https://fonts.googleapis.com/css2?family=Arimo:ital,wght@0,400;0,700;1,700&family=Tinos:wght@400;700&display=swap">
<style>
  :root {
    --page: #ffffff;
    --card-white: #ffffff;
    --kraft: #a58b73;
    --ink: #111111;
    --accent-red: #c8141c;
    --on-kraft: #ffffff;
    --mark: #2b3524;
    --rule-grey: #d6d6d6;
    --shadow: rgba(0, 0, 0, 0.38);
  }
  * { box-sizing: border-box; margin: 0; padding: 0; }
  html, body { width: 1200px; height: 900px; overflow: hidden; background: var(--page); }
  body { position: relative; font-family: "Arimo", Arial, sans-serif; color: var(--ink); }

  .card {
    position: absolute;
    width: 320px;
    height: 196px;
    background: var(--card-white);
    box-shadow: 7px 9px 12px var(--shadow);
    overflow: hidden;
  }
  .card--kraft { background: var(--kraft); color: var(--on-kraft); }
  .card--red { color: var(--accent-red); }

  .el { position: absolute; white-space: nowrap; line-height: 1; }
  .right { text-align: right; }
  .center { left: 0; right: 0; text-align: center; }

  .name-sans { font-weight: 700; font-size: 13px; letter-spacing: 0.2px; }
  .name-italic { font-weight: 700; font-style: italic; font-size: 14px; }
  .name-serif { font-family: "Tinos", "Times New Roman", serif; font-weight: 700; font-size: 13px; letter-spacing: 0.6px; }
  .creds-serif { font-family: "Tinos", "Times New Roman", serif; font-size: 8.5px; }
  .creds-sans { font-size: 9.5px; color: var(--accent-red); }
  .contact { font-size: 8px; }
  .address { font-size: 8px; }

  .brand { position: absolute; display: flex; align-items: center; gap: 5px; }
  .brand__dot { width: 40px; height: 40px; border-radius: 50%; background: var(--mark); flex: none; }
  .brand__name { font-size: 8px; font-weight: 700; white-space: nowrap; }

  .band { position: absolute; left: 0; top: 0; }
  .rule { position: absolute; }
</style>
</head>
<body>

<!-- Concept 1: black band front -->
<section class="card" style="left:71px;top:18px">
  <div class="el name-italic" style="left:14px;top:122px">MARNIE DOBROWEN</div>
  <div class="el creds-serif" style="left:22px;top:139px">(B.App.Sc.(TCM), Dip.Rem.Mass.)</div>
  <svg class="band" width="320" height="196" viewBox="0 0 320 196" aria-hidden="true">
    <polygon points="0,169 178,169 196,151 320,151 320,196 0,196" fill="#000"/>
  </svg>
  <div class="el contact right" style="right:12px;top:162px;color:#fff">Mob: 0491 570 313</div>
  <div class="el contact right" style="right:12px;top:176px;color:#fff">www.fernacupuncture-demo.com.au</div>
</section>

<section class="card" style="left:71px;top:232px">
  <div class="el address" style="left:14px;top:66px">The Quiet Grove &amp; Renewal Studio</div>
  <div class="el address" style="left:14px;top:84px">842 Brindle St, Camberwell VIC 3124</div>
  <div class="el address" style="left:14px;top:100px">Ph: 1300 482 177</div>
  <div class="rule" style="left:12px;top:115px;width:137px;height:3px;background:#000"></div>
  <div class="el address" style="left:14px;top:125px">Wattle Lane Integrative &amp; Restorative Care Clinic</div>
  <div class="el address" style="left:14px;top:141px">19 Ostler Rd, Malvern East VIC 3145</div>
  <div class="el address" style="left:14px;top:157px">Ph: (03) 9018 4472</div>
</section>

<!-- Concept 2: white with red -->
<section class="card" style="left:429px;top:22px">
  <div class="brand" style="left:14px;top:19px"><span class="brand__dot"></span><span class="brand__name">Fern Acupuncture</span></div>
  <div class="el name-sans" style="left:10px;top:152px">MARNIE DOBROWEN</div>
  <div class="el creds-sans" style="left:10px;top:167px">(B.App.Sc.(TCM), Dip.Rem.Mass.)</div>
  <div class="el contact right" style="right:12px;top:160px;color:var(--accent-red)">Mob: 0491 570 313</div>
  <div class="el contact right" style="right:12px;top:173px;color:var(--accent-red)">www.fernacupuncture-demo.com.au</div>
</section>

<section class="card card--red" style="left:429px;top:234px">
  <div class="el address" style="left:10px;top:67px">The Quiet Grove &amp; Renewal Studio</div>
  <div class="el address" style="left:10px;top:84px">842 Brindle St, Camberwell VIC 3124</div>
  <div class="el address" style="left:10px;top:100px">Ph: 1300 482 177</div>
  <div class="rule" style="left:10px;top:116px;width:138px;height:2px;background:var(--accent-red)"></div>
  <div class="el address" style="left:10px;top:123px">Wattle Lane Integrative &amp; Restorative Care Clinic</div>
  <div class="el address" style="left:10px;top:139px">19 Ostler Rd, Malvern East VIC 3145</div>
  <div class="el address" style="left:10px;top:155px">Ph: (03) 9018 4472</div>
</section>

<!-- Concept 3: kraft, name top right -->
<section class="card card--kraft" style="left:778px;top:22px">
  <div class="brand" style="left:19px;top:13px;flex-direction:column;align-items:flex-start;gap:3px"><span class="brand__dot"></span><span class="brand__name">Fern Acupuncture</span></div>
  <div class="el name-serif right" style="right:18px;top:19px;color:#111">MARNIE DOBROWEN</div>
  <div class="el creds-serif right" style="right:18px;top:34px">(B.App.Sc.(TCM), Dip.Rem.Mass.)</div>
  <div class="el contact right" style="right:10px;top:163px">Mob: 0491 570 313</div>
  <div class="el contact right" style="right:10px;top:177px">www.fernacupuncture-demo.com.au</div>
</section>

<section class="card card--kraft" style="left:778px;top:229px">
  <div class="el address center" style="top:64px">The Quiet Grove &amp; Renewal Studio</div>
  <div class="el address center" style="top:80px">842 Brindle St, Camberwell VIC 3124</div>
  <div class="el address center" style="top:96px">Ph: 1300 482 177</div>
  <div class="el address center" style="top:127px">Wattle Lane Integrative &amp; Restorative Care Clinic</div>
  <div class="el address center" style="top:143px">19 Ostler Rd, Malvern East VIC 3145</div>
  <div class="el address center" style="top:160px">Ph: (03) 9018 4472</div>
</section>

<!-- Concept 4: white, name top right with red credentials -->
<section class="card" style="left:71px;top:450px">
  <div class="el name-sans right" style="right:22px;top:12px;font-size:14px">MARNIE DOBROWEN</div>
  <div class="el creds-sans right" style="right:22px;top:31px">(B.App.Sc.(TCM), Dip.Rem.Mass.)</div>
  <div class="brand" style="left:18px;top:81px"><span class="brand__dot"></span><span class="brand__name">Fern Acupuncture</span></div>
  <div class="el contact right" style="right:15px;top:150px">Mob: 0491 570 313</div>
  <div class="el contact right" style="right:15px;top:164px">www.fernacupuncture-demo.com.au</div>
</section>

<section class="card" style="left:71px;top:660px">
  <div class="el address" style="left:14px;top:90px">The Quiet Grove &amp; Renewal Studio</div>
  <div class="el address" style="left:14px;top:107px">842 Brindle St, Camberwell VIC 3124</div>
  <div class="el address" style="left:14px;top:122px">Ph: 1300 482 177</div>
  <div class="rule" style="left:12px;top:136px;width:198px;height:1px;background:var(--rule-grey)"></div>
  <div class="el address" style="left:14px;top:143px">Wattle Lane Integrative &amp; Restorative Care Clinic</div>
  <div class="el address" style="left:14px;top:159px">19 Ostler Rd, Malvern East VIC 3145</div>
  <div class="el address" style="left:14px;top:175px">Ph: (03) 9018 4472</div>
</section>

<!-- Concept 5: kraft, centred name -->
<section class="card card--kraft" style="left:429px;top:446px">
  <div class="brand" style="right:12px;top:12px;flex-direction:column;align-items:flex-end;gap:3px"><span class="brand__dot"></span><span class="brand__name">Fern Acupuncture</span></div>
  <div class="el name-serif center" style="top:80px;color:#111">MARNIE DOBROWEN</div>
  <div class="el creds-serif center" style="top:96px">(B.App.Sc.(TCM), Dip.Rem.Mass.)</div>
  <div class="el contact" style="left:15px;top:171px">www.fernacupuncture-demo.com.au</div>
  <div class="el contact right" style="right:10px;top:171px">Mob: 0491 570 313</div>
</section>

<section class="card card--kraft" style="left:429px;top:679px">
  <div class="el address" style="left:12px;top:74px">The Quiet Grove &amp; Renewal Studio</div>
  <div class="el address" style="left:12px;top:90px">842 Brindle St, Camberwell VIC 3124</div>
  <div class="el address" style="left:12px;top:107px">Ph: 1300 482 177</div>
  <div class="el address" style="left:12px;top:132px">Wattle Lane Integrative &amp; Restorative Care Clinic</div>
  <div class="el address" style="left:12px;top:148px">19 Ostler Rd, Malvern East VIC 3145</div>
  <div class="el address" style="left:12px;top:164px">Ph: (03) 9018 4472</div>
</section>

<!-- Concept 6: white, centred -->
<section class="card" style="left:778px;top:450px">
  <div class="brand" style="left:0;right:0;top:44px;justify-content:center"><span class="brand__dot"></span><span class="brand__name">Fern Acupuncture</span></div>
  <div class="el name-serif center" style="top:117px">MARNIE DOBROWEN</div>
  <div class="el creds-serif center" style="top:132px">(B.App.Sc.(TCM), Dip.Rem.Mass.)</div>
  <div class="el contact center" style="top:174px">www.fernacupuncture-demo.com.au &nbsp; | &nbsp; Mob: 0491 570 313</div>
</section>

<section class="card" style="left:778px;top:679px">
  <div class="el address" style="left:9px;top:66px">The Quiet Grove &amp; Renewal Studio</div>
  <div class="el address" style="left:9px;top:82px">842 Brindle St, Camberwell VIC 3124</div>
  <div class="el address" style="left:9px;top:98px">Ph: 1300 482 177</div>
  <div class="rule" style="left:9px;top:114px;width:180px;height:9px;background:#000"></div>
  <div class="el address" style="left:9px;top:132px">Wattle Lane Integrative &amp; Restorative Care Clinic</div>
  <div class="el address" style="left:9px;top:148px">19 Ostler Rd, Malvern East VIC 3145</div>
  <div class="el address" style="left:9px;top:164px">Ph: (03) 9018 4472</div>
</section>

</body>
</html>
```